Flier redesign

Sample fliers are attached from previous 2 years "Seasonal care 2018" and "2019 Seasonal Care" . Need an updated design for this year.

Possible images are attached to this brief. If you use the before/after pictures - you should use both of them. Use images attached to this brief or any from our website that you may prefer.

Colors

Designer to choose colors to be used in the design.

Requirements
Must have
• Colors should match our website theme. www.hollowbrookgardens.org
• Should be a "new" design, not just copying one of the prior year designs with a different image.
• Must be created in photoshop and file must be provided at the end.
• Text should be the same as 2019 version.

```html
<!DOCTYPE html>
<html lang="en">
<head>
<meta charset="utf-8">
<title>Hollowbrook Gardens – 2020 Landscaping Packages</title>
<link rel="stylesheet" href="https://fonts.googleapis.com/css2?family=Montserrat:wght@500;700;800&family=Roboto:wght@400;500;700&family=Roboto+Condensed:wght@400;700&display=swap">
<style>
:root{
  --maroon:#7a1f2b;
  --maroon-dark:#4e121a;
  --earth:#7b3326;
  --earth-dark:#5f2519;
  --ink:#2f2f33;
  --body:#3d3d42;
  --card-top:#ffffff;
  --card-bottom:#e4e4e6;
  --footer-grey:#404043;
  --grass-light:#8cc45a;
  --grass-dark:#3f6b2a;
  --stone:#a4a6a3;
}
*{box-sizing:border-box;margin:0;padding:0}
html,body{width:703px;height:1200px;overflow:hidden;background:#fff}
body{font-family:"Roboto",sans-serif;color:var(--body);position:relative}

.header{position:absolute;left:0;top:0;width:703px;height:112px}
.brand{position:absolute;left:28px;top:44px;display:flex;align-items:center;gap:8px;white-space:nowrap}
.brand-dot{width:22px;height:22px;border-radius:50%;background:var(--maroon)}
.brand-name{font-family:"Roboto",sans-serif;font-weight:400;font-size:21px;color:var(--maroon);letter-spacing:.2px}
.headline{position:absolute;left:310px;top:40px;display:flex;align-items:baseline;gap:12px;white-space:nowrap}
.headline-year{font-family:"Montserrat",sans-serif;font-weight:800;font-size:34px;color:var(--maroon)}
.headline-title{font-family:"Roboto",sans-serif;font-weight:400;font-size:21px;color:var(--ink);letter-spacing:.2px}

.compare{position:absolute;top:112px;width:343px;height:488px;overflow:hidden}
.compare-before{left:0;border-bottom-left-radius:46px}
.compare-after{left:360px;border-bottom-right-radius:46px}
.compare-photo{position:absolute;left:0;top:0;width:100%;height:420px;
  background:linear-gradient(180deg,var(--stone) 0%,#8d958a 16%,var(--grass-dark) 34%,var(--grass-light) 72%,#6fae47 100%)}
.compare-band{position:absolute;left:0;bottom:0;width:100%;height:68px;
  background:linear-gradient(180deg,var(--earth) 0%,var(--earth-dark) 100%);
  display:flex;align-items:center;justify-content:center;
  font-family:"Montserrat",sans-serif;font-weight:800;font-size:31px;color:#fff}

.package{position:absolute;width:200px;bottom:100px;
  background:linear-gradient(180deg,var(--card-top) 0%,var(--card-bottom) 100%);
  border-radius:6px;box-shadow:0 3px 10px rgba(0,0,0,.16);padding:0 12px 0 16px}
.package-seasonal{left:29px;top:728px}
.package-basic{left:251px;top:696px}
.package-perpetual{left:474px;top:658px}

.package-tab{position:absolute;left:-10px;background:var(--maroon);color:#fff;
  font-family:"Montserrat",sans-serif;font-weight:800;font-size:14px;line-height:14px;
  padding:8px 14px 7px 24px;border-radius:0 6px 6px 0;text-transform:uppercase;white-space:nowrap}
.package-tab::after{content:"";position:absolute;left:0;bottom:-8px;border-top:8px solid var(--maroon-dark);border-left:8px solid transparent}
.package-seasonal .package-tab{top:32px;width:175px}
.package-basic .package-tab{top:36px;width:175px}
.package-perpetual .package-tab{top:24px;width:183px}

.package-lead{font-family:"Montserrat",sans-serif;font-weight:500;font-size:11.5px;line-height:13.5px;color:var(--ink);margin-bottom:12px}
.package-seasonal .package-lead{margin-top:76px;padding-right:40px}
.package-basic .package-lead{margin-top:100px;margin-bottom:18px}
.package-perpetual .package-lead{margin-top:80px;margin-bottom:14px}

.features{list-style:none}
.features li{position:relative;padding-left:18px;font-size:10.5px;line-height:12.8px;margin-bottom:8px;color:var(--body)}
.package-seasonal .features li{padding-right:30px}
.package-basic .features li{padding-right:20px}
.features li svg{position:absolute;left:0;top:2px;width:9px;height:9px}
.features b{font-weight:500;color:var(--ink)}
.features .accent{color:var(--maroon)}

.price-row{display:flex;align-items:center;justify-content:space-between;margin-top:8px}
.price-label{font-family:"Montserrat",sans-serif;font-weight:700;font-size:11.5px;line-height:13px;color:var(--ink);text-transform:uppercase;white-space:nowrap}
.price-box{border:1.5px solid var(--maroon);border-radius:7px;width:84px;height:28px;flex:none;
  display:flex;align-items:center;justify-content:center;color:var(--maroon);
  font-family:"Roboto Condensed",sans-serif;font-weight:400}
.price-box .cur{font-size:13px;font-weight:700;align-self:flex-start;margin-top:3px;margin-right:3px}
.price-box .amt{font-size:25px}
.package-seasonal .price-row{margin-top:10px;padding-right:14px}
.package-seasonal .price-label{padding-left:2px}
.package-basic .price-row,.package-perpetual .price-row{margin-top:18px}
.package-basic .price-box,.package-perpetual .price-box{width:76px}

.package-note{font-size:10.5px;line-height:12.5px;color:var(--body);margin-top:26px}
.package-seasonal .package-note{margin-top:22px}
.package-note .accent{color:var(--maroon)}

.footer{position:absolute;left:0;top:1122px;width:703px;height:78px}
.footer svg.footer-shape{position:absolute;left:0;top:0}
.contact{position:absolute;left:64px;top:26px;right:16px;height:46px;display:flex;align-items:center;gap:18px;color:#fff;white-space:nowrap}
.contact-item{display:flex;align-items:center;gap:7px;font-size:13px;white-space:nowrap}
.contact-phone{font-size:22px;font-weight:400}
.contact-item svg{flex:none}
</style>
</head>
<body>

<header class="header">
  <div class="brand">
    <span class="brand-dot"></span>
    <span class="brand-name">Hollowbrook Gardens</span>
  </div>
  <div class="headline">
    <span class="headline-year">2020</span>
    <span class="headline-title">LANDSCAPING PACKAGES</span>
  </div>
</header>

<section class="compare compare-before">
  <div class="compare-photo" role="img" aria-label="Photo of an overgrown gravesite with weeds in front of a granite headstone"></div>
  <div class="compare-band">Before</div>
</section>
<section class="compare compare-after">
  <div class="compare-photo" role="img" aria-label="Photo of the same gravesite after care, with a trimmed boxwood bed and clean marker"></div>
  <div class="compare-band">After</div>
</section>

<article class="package package-seasonal">
  <h2 class="package-tab">Seasonal Care</h2>
  <p class="package-lead">Seasonal landscaping grave care.</p>
  <ul class="features">
    <li><svg viewBox="0 0 10 10"><circle cx="5" cy="5" r="4.2" fill="none" stroke="#7a1f2b" stroke-width="1"/><path d="M3 5.2l1.5 1.5L7.2 3.6" fill="none" stroke="#7a1f2b" stroke-width="1.1"/></svg>Weeding and trimming services on your gravesite approximately every 7 weeks during the growing <span class="accent">season</span>: <b>mid-April through mid-October</b></li>
  </ul>
  <div class="price-row"><span class="price-label">3 Years</span><span class="price-box"><span class="cur">$</span><span class="amt">345</span></span></div>
  <div class="price-row"><span class="price-label">2 Years</span><span class="price-box"><span class="cur">$</span><span class="amt">230</span></span></div>
  <div class="price-row"><span class="price-label">1 Years</span><span class="price-box"><span class="cur">$</span><span class="amt">115</span></span></div>
  <p class="package-note">Multi-year payment locks in current rates.<span class="accent">Valid through 10/31/19.</span></p>
</article>

<article class="package package-basic">
  <h2 class="package-tab">Basic Careen<br>Dowment</h2>
  <p class="package-lead">Landscaping care forever<br>for graves with no plantings.</p>
  <ul class="features">
    <li><svg viewBox="0 0 10 10"><circle cx="5" cy="5" r="4.2" fill="none" stroke="#7a1f2b" stroke-width="1"/><path d="M3 5.2l1.5 1.5L7.2 3.6" fill="none" stroke="#7a1f2b" stroke-width="1.1"/></svg>Weeding and trimming services on your gravesite 2 times per year. <b>mid-May and mid-September</b></li>
    <li><svg viewBox="0 0 10 10"><circle cx="5" cy="5" r="4.2" fill="none" stroke="#7a1f2b" stroke-width="1"/><path d="M3 5.2l1.5 1.5L7.2 3.6" fill="none" stroke="#7a1f2b" stroke-width="1.1"/></svg>Monument leveling</li>
    <li><svg viewBox="0 0 10 10"><circle cx="5" cy="5" r="4.2" fill="none" stroke="#7a1f2b" stroke-width="1"/><path d="M3 5.2l1.5 1.5L7.2 3.6" fill="none" stroke="#7a1f2b" stroke-width="1.1"/></svg>Payment ensures grave</li>
  </ul>
  <div class="price-row"><span class="price-label">12 Monthly<br>Payments of</span><span class="price-box"><span class="cur">$</span><span class="amt">239</span></span></div>
  <p class="package-note">Call for single payment discount.<br><span class="accent">Valid through 10/31/19</span></p>
</article>

<article class="package package-perpetual">
  <h2 class="package-tab">Perpetual Care<br>Dowment</h2>
  <p class="package-lead">Landscaping care forever for graves with plantings.</p>
  <ul class="features">
    <li><svg viewBox="0 0 10 10"><circle cx="5" cy="5" r="4.2" fill="none" stroke="#7a1f2b" stroke-width="1"/><path d="M3 5.2l1.5 1.5L7.2 3.6" fill="none" stroke="#7a1f2b" stroke-width="1.1"/></svg>Weeding and triming services on your gravesite approximately every 7 weeks during the <span class="accent">growing season</span>: <b>mid-April through mid-October</b></li>
    <li><svg viewBox="0 0 10 10"><circle cx="5" cy="5" r="4.2" fill="none" stroke="#7a1f2b" stroke-width="1"/><path d="M3 5.2l1.5 1.5L7.2 3.6" fill="none" stroke="#7a1f2b" stroke-width="1.1"/></svg>Monument leveling and cleaning</li>
    <li><svg viewBox="0 0 10 10"><circle cx="5" cy="5" r="4.2" fill="none" stroke="#7a1f2b" stroke-width="1"/><path d="M3 5.2l1.5 1.5L7.2 3.6" fill="none" stroke="#7a1f2b" stroke-width="1.1"/></svg>Payment ensures grave care forever</li>
    <li><svg viewBox="0 0 10 10"><circle cx="5" cy="5" r="4.2" fill="none" stroke="#7a1f2b" stroke-width="1"/><path d="M3 5.2l1.5 1.5L7.2 3.6" fill="none" stroke="#7a1f2b" stroke-width="1.1"/></svg>Full bed of boxwood shrubs</li>
    <li><svg viewBox="0 0 10 10"><circle cx="5" cy="5" r="4.2" fill="none" stroke="#7a1f2b" stroke-width="1"/><path d="M3 5.2l1.5 1.5L7.2 3.6" fill="none" stroke="#7a1f2b" stroke-width="1.1"/></svg>Replacement of shrubs</li>
    <li><svg viewBox="0 0 10 10"><circle cx="5" cy="5" r="4.2" fill="none" stroke="#7a1f2b" stroke-width="1"/><path d="M3 5.2l1.5 1.5L7.2 3.6" fill="none" stroke="#7a1f2b" stroke-width="1.1"/></svg>Trust certificate</li>
  </ul>
  <div class="price-row"><span class="price-label">12 Monthly<br>Payments of</span><span class="price-box"><span class="cur">$</span><span class="amt">297</span></span></div>
  <p class="package-note">Call for single payment discount.<br><span class="accent">Valid through 10/31/19</span></p>
</article>

<footer class="footer">
  <svg class="footer-shape" width="703" height="78" viewBox="0 0 703 78">
    <rect x="0" y="0" width="703" height="78" fill="#7a1f2b"/>
    <path d="M0,78 Q18,24 80,18 H703 V78 Z" fill="#404043"/>
  </svg>
  <div class="contact">
    <span class="contact-item contact-phone">
      <svg width="20" height="20" viewBox="0 0 24 24"><path d="M6.6 10.8a15.1 15.1 0 0 0 6.6 6.6l2.2-2.2a1 1 0 0 1 1-.25 11.4 11.4 0 0 0 3.6.6 1 1 0 0 1 1 1V20a1 1 0 0 1-1 1A17 17 0 0 1 3 4a1 1 0 0 1 1-1h3.5a1 1 0 0 1 1 1 11.4 11.4 0 0 0 .6 3.6 1 1 0 0 1-.25 1z" fill="#fff"/><path d="M15 3a6 6 0 0 1 6 6M15 6.5a2.5 2.5 0 0 1 2.5 2.5" fill="none" stroke="#fff" stroke-width="1.6"/></svg>
      (201) 555-0148
    </span>
    <span class="contact-item">
      <svg width="12" height="12" viewBox="0 0 12 12"><circle cx="6" cy="6" r="5.3" fill="none" stroke="#fff" stroke-width="1.2"/><path d="M0.8 6h10.4M6 0.8c-2.4 2.8-2.4 7.6 0 10.4M6 0.8c2.4 2.8 2.4 7.6 0 10.4" fill="none" stroke="#fff" stroke-width="1"/></svg>
      www.hollowbrookgardens.org
    </span>
    <span class="contact-item">
      <svg width="15" height="11" viewBox="0 0 15 11"><rect x="0.6" y="0.6" width="13.8" height="9.8" fill="none" stroke="#fff" stroke-width="1.2"/><path d="M0.8 0.8l6.7 5.4 6.7-5.4" fill="none" stroke="#fff" stroke-width="1.2"/></svg>
      info@hollowbrookgardens.org
    </span>
  </div>
</footer>

</body>
</html>
```